Business card design needed

We are a wine business involved in winemaking, broking and packaging on behalf of clients globally with the majority being Asian. The design should be quite traditional and classic with some red used, font used should be easily read.

Target Market(s)

Trade customers other business owners

Industry/Entity Type

Business

Contact Information for Business Card

Rosalind Thwaite
Meridale Wine Collective
PO Box 738, Fenwick Vale
South Australia 5187
Phone: +61 (0)455 982 317
Email: kvcellars@brightmail.example

Logo styles of interest
Lettermark Logo

```html
<!DOCTYPE html>
<html lang="en">
<head>
<meta charset="utf-8">
<title>Meridale Wine Collective – Business Card</title>
<link rel="stylesheet" href="https://fonts.googleapis.com/css2?family=Cinzel:wght@400;600&display=swap">
<style>
  :root {
    --backdrop: #e9e4de;
    --card-black: #000000;
    --ink-white: #ffffff;
    --wine-red: #e41e26;
    --card-shadow: rgba(0, 0, 0, 0.35);
  }
  * { margin: 0; padding: 0; box-sizing: border-box; }
  html, body {
    width: 1200px;
    height: 800px;
    overflow: hidden;
    background: var(--backdrop);
  }
  .canvas {
    position: relative;
    width: 1200px;
    height: 800px;
    font-family: "Cinzel", "Times New Roman", serif;
    color: var(--ink-white);
  }
  .card {
    position: absolute;
    width: 619px;
    height: 381px;
    background: var(--card-black);
    box-shadow: 0 6px 18px var(--card-shadow);
  }
  .card--front { left: 118px; top: 64px; }
  .card--back  { left: 464px; top: 354px; }

  /* Front */
  .brand {
    position: absolute;
    left: 0; right: 0;
    top: 110px;
    text-align: center;
  }
  .brand__dot {
    display: block;
    width: 74px;
    height: 74px;
    margin: 0 auto 38px;
    border-radius: 50%;
    background: var(--wine-red);
  }
  .brand__name {
    font-size: 19px;
    font-weight: 400;
    letter-spacing: 0.06em;
  }

  /* Back */
  .person {
    position: absolute;
    left: 0; right: 0;
    top: 115px;
    text-align: center;
  }
  .person__name {
    font-size: 27px;
    font-weight: 600;
    letter-spacing: 0.03em;
    line-height: 1.1;
  }
  .person__role {
    margin-top: 6px;
    font-size: 14px;
    letter-spacing: 0.08em;
  }
  .contact {
    position: absolute;
    left: 0; right: 0;
    top: 252px;
    text-align: center;
    font-size: 15px;
    line-height: 21.5px;
    letter-spacing: 0.03em;
    font-style: normal;
  }
  .accent-band {
    position: absolute;
    left: 0; right: 0;
    bottom: 8px;
    height: 24px;
    background: var(--wine-red);
  }
</style>
</head>
<body>
<main class="canvas">
  <section class="card card--front" aria-label="Card front">
    <div class="brand">
      <span class="brand__dot" aria-hidden="true"></span>
      <p class="brand__name">Meridale Wine Collective</p>
    </div>
  </section>

  <section class="card card--back" aria-label="Card back">
    <div class="person">
      <h1 class="person__name">Rosalind Thwaite</h1>
      <p class="person__role">OWNER</p>
    </div>
    <address class="contact">
      PO BOX 738, FENWICK VALE SOUTH AUSTRALIA 5187<br>
      +61 (0)455 982 317<br>
      KVCELLARS@BRIGHTMAIL.EXAMPLE
    </address>
    <div class="accent-band"></div>
  </section>
</main>
</body>
</html>
```